Frizzle! A stand up comedy show- poster and other graphics required

We require a design for a new late night comedy show called 'Frizzle!' which will appear at festivals and feature a variety of stand up acts as well as inviting the audience to heckle the comedians on stage. The final design should be bold and stand out loudly, to fit the late night raucous nature of the show.
We need a poster image as well as smaller images for program guides and websites. This is going to be the kind of show people talk about so needs a poster to match!!

Target Market(s)

Comedy fans, 20-40 year olds, late night adult audience

Requirements
Nice to have
• We don't really have any clear design in mind so happy to leave it to interpretation but possible ideas would be: a silhouette of a head shouting / a mic is always an iconic image / the simple outline of an audience with obscenities (@*!& etc) coming out of them / perhaps a mic having fallen over because of a stand-up running off stage!
• But again these are vague ideas. Please message for more info about the show if it helps
Should not have
• Not too busy

```html
<!DOCTYPE html>
<html lang="en">
<head>
<meta charset="utf-8">
<title>Frizzle! – Stand Up Comedy Poster</title>
<link rel="stylesheet" href="https://fonts.googleapis.com/css2?family=Arimo:wght@400;700&display=swap">
<style>
  :root {
    --stage-grey: #808080;
    --poster-black: #000000;
    --signal-red: #ff0000;
    --mic-red: #9b0000;
    --banner-yellow: #e6ff00;
    --text-yellow: #ffff00;
    --text-white: #ffffff;
  }
  html, body {
    margin: 0;
    padding: 0;
    width: 914px;
    height: 1200px;
    overflow: hidden;
    background: var(--stage-grey);
  }
  .canvas {
    position: relative;
    width: 914px;
    height: 1200px;
    font-family: "Arimo", Arial, sans-serif;
  }
  .poster {
    position: absolute;
    left: 123px;
    top: 127px;
    width: 668px;
    height: 946px;
    background: var(--poster-black);
    overflow: hidden;
  }
  .poster-art {
    position: absolute;
    left: 0;
    top: 0;
  }
  .show-name {
    font-family: "Arimo", Arial, sans-serif;
    font-weight: 700;
    font-size: 82px;
    fill: var(--text-yellow);
  }
  .tagline {
    font-family: "Arimo", Arial, sans-serif;
    font-weight: 700;
    font-size: 28px;
    fill: var(--signal-red);
  }
  .pitch {
    position: absolute;
    left: 329px;
    top: 633px;
    margin: 0;
    color: var(--text-yellow);
    font-size: 23px;
    line-height: 27px;
    font-weight: 400;
    text-transform: uppercase;
  }
  .event-details {
    position: absolute;
    left: 329px;
    top: 781px;
    margin: 0;
    padding: 0;
    list-style: none;
    color: var(--text-white);
    font-weight: 700;
    font-size: 22px;
  }
  .event-details li {
    height: 55px;
  }
</style>
</head>
<body>
<div class="canvas">
  <section class="poster">
    <svg class="poster-art" width="668" height="946" viewBox="0 0 668 946">
      <defs>
        <radialGradient id="mic-glow" cx="50%" cy="50%" r="50%">
          <stop offset="0" stop-color="var(--mic-red)"/>
          <stop offset="0.7" stop-color="var(--mic-red)"/>
          <stop offset="1" stop-color="var(--mic-red)" stop-opacity="0"/>
        </radialGradient>
      </defs>

      <circle cx="332" cy="343" r="243" fill="none" stroke="var(--signal-red)" stroke-width="9"/>

      <rect class="mic-illustration" x="236" y="262" width="180" height="180"
            fill="url(#mic-glow)" role="img" aria-label="Illustration of a vintage stage microphone"/>

      <text class="show-name" x="332" y="250" text-anchor="middle">FRIZZLE!</text>

      <g class="banner">
        <polygon points="40,476 617,378 628,485 66,591" fill="var(--signal-red)"/>
        <polygon points="56,484 606,392 614,475 78,578" fill="var(--banner-yellow)"/>
        <text class="tagline" x="331" y="494" text-anchor="middle" transform="rotate(-9.5 331 485)">A VARIETY OF STAND UP ACTS</text>
      </g>
    </svg>

    <p class="pitch">Inviting<br>the audience<br>to heckle<br>the comedians<br>on stage</p>

    <ul class="event-details">
      <li>Date:</li>
      <li>Time:</li>
      <li>Venue:</li>
    </ul>
  </section>
</div>
</body>
</html>
```